Business Cards Design for the electrical wholesaler: clean bold dynamic :)

We need a business card design that would follow our latest brand guidelines. As an electrical wholesaler we want to bring a fresh look and feel into the industry. The design should be clean bold and dynamic. It should come alive with the renewed energy of our green colour. Our grey colour should keep things balanced and complement the notion of maturity and responsibility. We employ Lato as a corporate font however are not bound by this font and we’re open to interpretation here.

Target Market(s)

Electrical contractors

Industry/Entity Type

Business

Contact Information for Business Card

Logo
Name & Surname: Olena Dovbush
Job Title: Director of Marketing
Email: helen.dovbush@mailvane.example
Cell phone: XXX.XXX.XXXX
Address: 20917 - 87 Ave. Edmonton, AB, Canada. T6K 2R8
Business Phone: 780.555.0187
Website: www.qorvil.example

Font styles to use
Other font styles liked:
• Lato

Requirements
Must have
• Logo & website
Nice to have
• Brand elements - some of them you may find in the attached Brand Guidelines (e.g. three lines on the background signifying "W")

```html
<!DOCTYPE html>
<html lang="en">
<head>
<meta charset="utf-8">
<title>Qorvil Electrical Wholesalers – Business Cards</title>
<link rel="stylesheet" href="https://fonts.googleapis.com/css2?family=Lato:wght@400;700;900&display=swap">
<style>
  :root {
    --page: #e9e8e6;
    --card-white: #fbfbfb;
    --grey-dark: #3d3d3d;
    --grey-mid: #5a5a5a;
    --grey-soft: #6e6e6e;
    --green: #7dc242;
    --ink: #2f2f2f;
    --white: #ffffff;
  }
  * { box-sizing: border-box; margin: 0; padding: 0; }
  html, body { width: 1200px; height: 800px; overflow: hidden; }
  body {
    background: var(--page);
    font-family: "Lato", Arial, sans-serif;
    position: relative;
  }
  .card {
    position: absolute;
    width: 525px;
    height: 300px;
    border-radius: 4px;
    box-shadow: 0 8px 24px rgba(0,0,0,0.14);
    overflow: hidden;
  }
  .card--front { left: 50px; top: 250px; background: var(--card-white); }
  .card--back { left: 625px; top: 250px; background: linear-gradient(135deg, var(--grey-mid) 0%, var(--grey-dark) 100%); color: var(--white); }

  .texture {
    position: absolute; inset: 0;
  }
  .card--front .texture { background: radial-gradient(ellipse at 60% 50%, #f1f1f1 0%, var(--card-white) 70%); }
  .card--back .texture { background: linear-gradient(120deg, rgba(255,255,255,0) 30%, rgba(255,255,255,0.07) 60%, rgba(255,255,255,0.12) 100%); }

  .brand { position: absolute; display: flex; flex-direction: column; align-items: flex-end; }
  .brand__row { display: flex; align-items: center; gap: 12px; }
  .brand__dot { width: 30px; height: 30px; border-radius: 50%; background: var(--green); }
  .brand__name { font-weight: 900; font-size: 58px; line-height: 1; letter-spacing: -1px; }
  .brand__tag { font-weight: 400; font-size: 12px; letter-spacing: 0.4px; text-transform: uppercase; margin-top: 4px; }

  .card--front .brand { left: 118px; top: 105px; }
  .card--front .brand__name { color: var(--ink); }
  .card--front .brand__tag { color: var(--ink); }

  .card--back .brand { right: 34px; top: 42px; }
  .card--back .brand__name { color: var(--white); font-size: 50px; }
  .card--back .brand__tag { color: var(--white); font-size: 11px; }

  .contact { position: absolute; left: 28px; top: 62px; list-style: none; font-size: 13.5px; line-height: 19px; }
  .contact li { display: flex; align-items: flex-start; gap: 8px; }
  .contact svg { width: 12px; height: 12px; margin-top: 3px; flex: none; fill: var(--green); }
  .contact .address { padding-left: 20px; }

  .divider { position: absolute; left: 268px; top: 172px; width: 2px; height: 86px; background: var(--white); transform: rotate(22deg); }

  .person { position: absolute; right: 40px; bottom: 42px; text-align: left; }
  .person__name { color: var(--green); font-weight: 900; font-size: 24px; }
  .person__title { color: var(--white); font-weight: 700; font-size: 13.5px; margin-top: 2px; }
</style>
</head>
<body>

<section class="card card--front" aria-label="Business card front">
  <div class="texture" role="img" aria-label="Faint hexagon pattern texture"></div>
  <div class="brand">
    <div class="brand__row">
      <span class="brand__dot"></span>
      <span class="brand__name">qorvil</span>
    </div>
    <span class="brand__tag">Electrical Wholesalers</span>
  </div>
</section>

<section class="card card--back" aria-label="Business card back">
  <div class="texture" role="img" aria-label="Dark hexagon pattern with large faint brand shape"></div>

  <div class="brand">
    <div class="brand__row">
      <span class="brand__dot"></span>
      <span class="brand__name">qorvil</span>
    </div>
    <span class="brand__tag">Electrical Wholesalers</span>
  </div>

  <ul class="contact">
    <li><svg viewBox="0 0 12 12"><path d="M0 2h12v8H0z M1 3l5 3.5L11 3v-.2H1z" fill-rule="evenodd"/></svg>helen.dovbush@mailvane.example</li>
    <li><svg viewBox="0 0 12 12"><path d="M3 0h6a1 1 0 0 1 1 1v10a1 1 0 0 1-1 1H3a1 1 0 0 1-1-1V1a1 1 0 0 1 1-1zm0 1.5v8h6v-8z"/></svg>XXX.XXX.XXXX</li>
    <li><svg viewBox="0 0 12 12"><circle cx="6" cy="6" r="6"/><path d="M3.5 3l1.3-.3.8 1.8-.8.6a5 5 0 0 0 2 2l.6-.8 1.8.8-.3 1.3C6 8.5 3.5 6 3.5 3z" fill="#3d3d3d"/></svg>780.555.0187</li>
    <li><svg viewBox="0 0 12 12"><circle cx="6" cy="6" r="6"/><path d="M1 6h10M6 1c-2 2.5-2 7.5 0 10M6 1c2 2.5 2 7.5 0 10" stroke="#3d3d3d" stroke-width="0.8" fill="none"/></svg>www.qorvil.example</li>
    <li><svg viewBox="0 0 12 12"><path d="M6 0.5L0 6h1.8v5.5h3V8h2.4v3.5h3V6H12z"/></svg>20917 - 87 Ave.</li>
    <li class="address">Edmonton, AB, Canada. T6K 2R8</li>
  </ul>

  <span class="divider"></span>

  <div class="person">
    <p class="person__name">Olena Dovbush</p>
    <p class="person__title">Director of Marketing</p>
  </div>
</section>

</body>
</html>
```